Mortgage Loan Program(s) for Furloughed Federal Government Workers

Mortgage Loan Program(s)
For
Furloughed Federal Government Workers

* Preserve Your Credit Rating
* Receive Cash out to Increase Savings or Consolidate Bills
* Close in 30 Days or Less
* FHA and Conventional Loan Programs
* Very Competitive Rates Available
* DC & MD Properties Only

You deserve better. Contact us today....

Office (800) 647-2914 x23
Cell (240) 486-2079
Email mkowalczyk@brightpathlending.example

Marcus Kowalczyk
Brightpath Lending Services, Inc.
NMLS #837160 / #56408

Target Market(s)

```html
<!DOCTYPE html>
<html lang="en">
<head>
<meta charset="utf-8">
<title>Mortgage Loan Program(s) for Furloughed Federal Government Workers</title>
<link rel="stylesheet" href="https://fonts.googleapis.com/css2?family=Montserrat:wght@700;800&family=Raleway:wght@400;500;700&family=Lora:ital,wght@1,400;1,500&family=Roboto+Condensed:wght@700&display=swap">
<style>
  :root {
    --green: #1b9a45;
    --blue: #1b5cab;
    --navy: #213f96;
    --panel: #f1f1f3;
    --ink: #444;
    --white: #ffffff;
  }
  * { margin: 0; padding: 0; box-sizing: border-box; }
  html, body { width: 946px; height: 1200px; overflow: hidden; background: var(--white); }
  .flyer { position: relative; width: 946px; height: 1200px; overflow: hidden; background: var(--white); }
  .backdrop { position: absolute; inset: 0; }
  .hero-photo { position: absolute; inset: 0; }

  .brand {
    position: absolute; left: 34px; top: 318px; width: 200px;
    font-family: "Raleway", sans-serif; font-weight: 700; font-size: 17px;
    color: var(--blue); line-height: 1.25; display: flex; align-items: center; gap: 10px;
  }
  .brand-mark { width: 24px; height: 24px; border-radius: 50%; background: var(--blue); flex: none; }

  .info-panel {
    position: absolute; left: 10px; top: 475px; width: 650px; height: 687px;
    background: var(--panel); border: 6px solid var(--green); border-left: none;
    border-radius: 0 46px 46px 0;
  }
  .title {
    position: absolute; left: 0; width: 100%; top: 56px; text-align: center;
    font-family: "Montserrat", sans-serif; font-weight: 800; font-size: 56px; line-height: 66px; letter-spacing: -0.5px;
  }
  .title .line-green { color: var(--green); display: block; }
  .title .line-blue { color: var(--blue); display: block; }
  .subtitle {
    position: absolute; left: 0; width: 100%; top: 190px; text-align: center;
    font-family: "Lora", serif; font-style: italic; font-size: 30px; line-height: 40px;
  }
  .subtitle .for { color: var(--green); display: block; }
  .subtitle .audience { color: var(--blue); display: block; }
  .rule { position: absolute; left: 288px; top: 287px; width: 98px; height: 2px; background: #555; }
  .features-heading {
    position: absolute; left: 0; width: 100%; top: 330px; text-align: center;
    font-family: "Raleway", sans-serif; font-weight: 400; font-size: 28px; color: var(--green);
  }
  .features { position: absolute; left: 36px; top: 390px; width: 590px; list-style: none; display: grid; grid-template-columns: 305px 285px; row-gap: 16px; }
  .feature { display: flex; align-items: center; gap: 16px; height: 42px; }
  .feature-icon {
    width: 38px; height: 38px; border-radius: 50%; background: var(--navy); flex: none;
    border: 2px solid #9fb0dc; display: flex; align-items: center; justify-content: center;
    color: var(--white); font-family: "Roboto Condensed", sans-serif; font-weight: 700; font-size: 17px; line-height: 1;
  }
  .feature-text { font-family: "Lora", serif; font-style: italic; font-size: 15px; line-height: 17px; color: var(--ink); }

  .cta-band {
    position: absolute; left: 0; top: 552px; width: 644px; height: 58px; background: var(--green);
    font-family: "Lora", serif; font-style: italic; font-weight: 500; font-size: 33px; color: var(--white);
    padding-left: 36px; line-height: 58px; white-space: nowrap;
  }
  .signature {
    position: absolute; left: 34px; top: 626px; font-family: "Raleway", sans-serif; font-size: 19.5px; color: #555; white-space: nowrap;
  }
  .signature .name { color: var(--navy); font-weight: 700; }

  .side-photo { position: absolute; border: 3px solid var(--blue); }
  .photo-stress { left: 694px; top: 460px; width: 226px; height: 158px; background: linear-gradient(135deg, #b9b2ab, #6e5d52 60%, #9a7b60); }
  .photo-review { left: 694px; top: 634px; width: 226px; height: 242px; background: linear-gradient(160deg, #c9c9cc, #5f5f69 55%, #7a6b5c); clip-path: polygon(0 0, 100% 0, 100% 74%, 0 100%); }
  .photo-advisor { left: 696px; top: 822px; width: 222px; height: 206px; background: linear-gradient(160deg, #4a6aa0, #2c3d66 60%, #1a1d28); clip-path: polygon(0 33%, 100% 0, 100% 100%, 0 100%); border: none; }

  .contact { position: absolute; left: 696px; top: 1050px; width: 240px; list-style: none; font-family: "Roboto Condensed", sans-serif; font-weight: 700; color: var(--white); }
  .contact li { display: flex; align-items: center; gap: 14px; height: 30px; font-size: 15.5px; white-space: nowrap; }
  .contact li.email { font-size: 11px; letter-spacing: -0.1px; }
  .contact svg { width: 20px; height: 20px; flex: none; }
</style>
</head>
<body>
<main class="flyer">
  <svg class="backdrop" width="946" height="1200" viewBox="0 0 946 1200" aria-hidden="true">
    <polygon points="0,0 946,0 946,335 610,478 0,478" fill="#ffffff"/>
    <polygon points="0,18 14,0 310,478 278,478" fill="var(--green)"/>
    <polygon points="946,335 946,375 650,478 600,478" fill="var(--green)"/>
    <polygon points="660,930 946,820 946,1200 660,1200" fill="var(--navy)"/>
    <polygon points="0,1200 660,1160 660,1200" fill="var(--navy)"/>
    <polygon points="946,1130 946,1200 790,1200" fill="var(--green)"/>
    <polygon points="0,1050 10,1050 10,1200 0,1200" fill="var(--green)"/>
  </svg>

  <svg class="hero-photo" width="946" height="1200" viewBox="0 0 946 1200" role="img" aria-label="Silhouette of a person with raised arms at the bright end of a stone tunnel">
    <defs>
      <radialGradient id="tunnelLight" cx="0.55" cy="0.45" r="0.6">
        <stop offset="0" stop-color="#fff6df"/>
        <stop offset="0.18" stop-color="#e0a86a"/>
        <stop offset="0.5" stop-color="#6a4326"/>
        <stop offset="1" stop-color="#120d0a"/>
      </radialGradient>
    </defs>
    <polygon points="16,0 946,0 946,335 610,478 300,478" fill="url(#tunnelLight)"/>
  </svg>

  <svg class="backdrop" width="946" height="1200" viewBox="0 0 946 1200" aria-hidden="true">
    <polygon points="0,165 176,165 348,436 0,436" fill="var(--blue)"/>
    <polygon points="22,184 166,184 314,418 22,418" fill="#ffffff"/>
  </svg>
  <div class="brand"><span class="brand-mark"></span>Brightpath Lending Services, Inc.</div>

  <section class="info-panel">
    <h1 class="title"><span class="line-green">MORTGAGE LOAN</span><span class="line-blue">PROGRAM(S)</span></h1>
    <p class="subtitle"><span class="for">For</span><span class="audience">Furloughed Federal Government Workers</span></p>
    <div class="rule"></div>
    <h2 class="features-heading">Our Features</h2>
    <ul class="features">
      <li class="feature"><span class="feature-icon"><svg width="20" height="14" viewBox="0 0 20 14"><path d="M2 12a8 8 0 0 1 16 0" fill="none" stroke="#fff" stroke-width="2"/><line x1="10" y1="12" x2="14" y2="6" stroke="#fff" stroke-width="2"/></svg></span><span class="feature-text">Preserve Your Credit Rating</span></li>
      <li class="feature"><span class="feature-icon"><svg width="20" height="20" viewBox="0 0 20 20"><path d="M3 10 10 3l7 7v8H3z" fill="none" stroke="#fff" stroke-width="2"/><path d="M6 13l3 3 5-6" fill="none" stroke="#fff" stroke-width="2"/></svg></span><span class="feature-text">FHA and Conventional<br>Loan Programs</span></li>
      <li class="feature"><span class="feature-icon"><svg width="16" height="20" viewBox="0 0 16 20"><rect x="2" y="1" width="12" height="18" fill="none" stroke="#fff" stroke-width="2"/><line x1="5" y1="7" x2="11" y2="7" stroke="#fff" stroke-width="2"/><line x1="5" y1="11" x2="11" y2="11" stroke="#fff" stroke-width="2"/><line x1="5" y1="15" x2="11" y2="15" stroke="#fff" stroke-width="2"/></svg></span><span class="feature-text">Receive Cash out to Increase<br>Savings or Consolidate Bills</span></li>
      <li class="feature"><span class="feature-icon"><svg width="20" height="18" viewBox="0 0 20 18"><path d="M10 1 1 9h3v8h5v-5h2v5h5V9h3z" fill="#fff"/></svg></span><span class="feature-text">DC &amp; MD Properties Only</span></li>
      <li class="feature"><span class="feature-icon">30</span><span class="feature-text">Close in 30 Days or Less</span></li>
      <li class="feature"><span class="feature-icon"><svg width="18" height="18" viewBox="0 0 18 18"><rect x="1" y="9" width="4" height="8" fill="#fff"/><rect x="7" y="3" width="4" height="14" fill="#fff"/><rect x="13" y="7" width="4" height="10" fill="#fff"/></svg></span><span class="feature-text">Very Competitive Rates<br>Available</span></li>
    </ul>
    <p class="cta-band">You deserve better. Contact us today....</p>
    <p class="signature"><span class="name">Marcus Kowalczyk |</span> Brightpath Lending Services, Inc. | NMLS</p>
  </section>

  <div class="side-photo photo-stress" role="img" aria-label="Worried couple with bills, one holding a help sign"></div>
  <div class="side-photo photo-review" role="img" aria-label="Couple sitting together reviewing paperwork"></div>
  <div class="side-photo photo-advisor" role="img" aria-label="Portrait of the loan officer in a suit and tie"></div>

  <ul class="contact">
    <li><svg viewBox="0 0 20 20"><path d="M4 2l4 1 1 4-2 2a11 11 0 0 0 4 4l2-2 4 1 1 4-3 2C9 18 2 11 2 5z" fill="#fff"/></svg>(800) 647-2914 x23</li>
    <li><svg viewBox="0 0 20 20"><rect x="5" y="1" width="10" height="18" rx="2" fill="none" stroke="#fff" stroke-width="2"/><line x1="9" y1="16" x2="11" y2="16" stroke="#fff" stroke-width="2"/></svg>(240) 486-2079</li>
    <li class="email"><svg viewBox="0 0 20 20"><rect x="1" y="4" width="18" height="12" fill="#fff"/><path d="M1 4l9 7 9-7" fill="none" stroke="var(--navy)" stroke-width="1.5"/></svg>mkowalczyk@brightpathlending.example</li>
  </ul>
</main>
</body>
</html>
```